Mindfulness School for Children -- Business Cards

We're looking for business cards for our school directors and owners. We're a mindfulness school for children called tumbling willows. Attached are our logos/icons.

```html
<!DOCTYPE html>
<html lang="en">
<head>
<meta charset="utf-8">
<title>Tumbling Willows — Business Cards</title>
<link rel="stylesheet" href="https://fonts.googleapis.com/css2?family=Alegreya:wght@500&family=Montserrat:wght@500;700&family=Roboto:wght@500&display=swap">
<style>
  :root {
    --page: #eeeeee;
    --sky: #74cde6;
    --navy: #0c4a85;
    --white: #ffffff;
    --teal: #5aa9bf;
  }
  * { margin: 0; padding: 0; box-sizing: border-box; }
  html, body { width: 959px; height: 1200px; overflow: hidden; background: var(--page); }
  .canvas { position: relative; width: 959px; height: 1200px; }

  .card {
    position: absolute;
    background: var(--sky);
    overflow: hidden;
    box-shadow: 0 1px 4px rgba(0,0,0,0.25);
  }

  /* Front */
  .card-front { left: 126px; top: 126px; width: 706px; height: 403px; }
  .edge-tab { position: absolute; top: 153px; width: 16px; height: 97px; background: var(--white); }
  .edge-tab.left { left: 0; }
  .edge-tab.right { right: 0; }
  .front-name {
    position: absolute; left: 0; right: 0; top: 168px;
    text-align: center;
    font-family: "Alegreya", Georgia, serif;
    font-weight: 500; font-size: 54px; line-height: 1;
    color: var(--white);
  }
  .front-web {
    position: absolute; left: 0; right: 0; top: 358px;
    text-align: center;
    font-family: "Montserrat", Arial, sans-serif;
    font-weight: 500; font-size: 15px; letter-spacing: 1.6px;
    color: var(--white);
  }

  /* Back */
  .card-back { left: 122px; top: 667px; width: 711px; height: 406px; }
  .brand-panel { position: absolute; left: 0; top: 0; width: 198px; height: 100%; background: var(--white); }
  .brand-vertical {
    position: absolute; left: 114px; top: 191px;
    transform: translate(-50%, -50%) rotate(-90deg);
    white-space: nowrap;
    font-family: "Alegreya", Georgia, serif;
    font-weight: 500; font-size: 42px; line-height: 1;
    color: var(--teal);
  }
  .person-name {
    position: absolute; left: 234px; top: 70px;
    font-family: "Montserrat", Arial, sans-serif;
    font-weight: 700; font-size: 33px; letter-spacing: 2px;
    color: var(--navy);
  }
  .person-role {
    position: absolute; left: 240px; top: 114px;
    font-family: "Montserrat", Arial, sans-serif;
    font-weight: 500; font-size: 13.5px; letter-spacing: 3.2px;
    color: var(--navy);
  }
  .role-rule { position: absolute; left: 241px; top: 137px; width: 87px; height: 2px; background: var(--navy); }

  .icon-rail {
    position: absolute; left: 239px; top: 167px; width: 32px; height: 167px;
    background: var(--navy); border-radius: 16px;
  }
  .icon-rail svg { position: absolute; left: 7px; width: 18px; height: 18px; fill: var(--white); }

  .contact-list { list-style: none; }
  .contact-list li {
    position: absolute; left: 289px;
    font-family: "Roboto", Arial, sans-serif;
    font-weight: 500; font-size: 17px; line-height: 20px;
    color: var(--navy);
    white-space: nowrap;
    transform: translateY(-50%);
  }
</style>
</head>
<body>
<div class="canvas">

  <section class="card card-front" aria-label="Card front">
    <span class="edge-tab left"></span>
    <span class="edge-tab right"></span>
    <h1 class="front-name">tumbling willows</h1>
    <p class="front-web">www.tumblingwillows.example</p>
  </section>

  <section class="card card-back" aria-label="Card back">
    <div class="brand-panel">
      <p class="brand-vertical">tumbling willows</p>
    </div>

    <h2 class="person-name">YOUR NAME</h2>
    <p class="person-role">DESIGNATION</p>
    <span class="role-rule"></span>

    <div class="icon-rail" aria-hidden="true">
      <svg viewBox="0 0 24 24" style="top:16px"><path d="M12 2a7 7 0 0 0-7 7c0 5 7 13 7 13s7-8 7-13a7 7 0 0 0-7-7zm0 9.5A2.5 2.5 0 1 1 12 6.5a2.5 2.5 0 0 1 0 5z"/></svg>
      <svg viewBox="0 0 24 24" style="top:55px"><path d="M6.6 10.8a15 15 0 0 0 6.6 6.6l2.2-2.2c.3-.3.7-.4 1-.2 1.1.4 2.3.6 3.6.6.6 0 1 .4 1 1V20c0 .6-.4 1-1 1A17 17 0 0 1 3 4c0-.6.4-1 1-1h3.5c.6 0 1 .4 1 1 0 1.3.2 2.5.6 3.6.1.3 0 .7-.2 1z"/></svg>
      <svg viewBox="0 0 24 24" style="top:94px"><path d="M2 5h20v14H2zm1.6 1.2L12 12.3l8.4-6.1zM3.2 17.8l6.2-5.4-6.2-4.4zm17.6 0V8l-6.2 4.4zM4.4 17.8h15.2l-5.9-5.1L12 14l-1.7-1.3z" fill-rule="evenodd"/></svg>
      <svg viewBox="0 0 24 24" style="top:133px"><path d="M6 2v17l4.2-4 3 7 2.6-1.1-3-6.8H18z"/></svg>
    </div>

    <ul class="contact-list">
      <li style="top:192px">YOUR ADDRESS HERE</li>
      <li style="top:231px">+00 111 222 78</li>
      <li style="top:270px">companyname@example.com</li>
      <li style="top:309px">www.companysite.example</li>
    </ul>
  </section>

</div>
</body>
</html>
```